Company Powerpoint template - Bright Lantern Works

I need a company powerpoint template for Bright Lantern Works that has a number of templated slides with an exciting supporting colour palette. Needs to have header and footer sections, tables in colour which support the logo colour, bar and line charts, dot point slides and image (placeholders) slides. Logo is attached.
The primary use of this template is to pitch for new work - ie about us page, previous clients page, then a breakdown of services offered in a table format with prices etc...

Target Market(s)

small to medium businesses - look is proessional, but edgy and exciting

Industry/Entity Type

Management Consulting

Font styles to use
Sans Serif

Requirements
Must have
• See project description.
Nice to have
• I like the use of gradient in colour
Should not have
• No drop shadow or 3d options - just clean flat design

```html
<!DOCTYPE html>
<html lang="en">
<head>
<meta charset="utf-8">
<title>Bright Lantern Works – Company Presentation Template</title>
<link href="https://fonts.googleapis.com/css2?family=Abel&family=Open+Sans:wght@400;600;700&display=swap" rel="stylesheet">
<style>
:root{
  --green:#8cc63f;
  --lime:#a8d45a;
  --teal:#3fb6a8;
  --blue:#2d9fd8;
  --ink:#1f1f1f;
  --text:#7a7a7a;
  --soft:#ececec;
  --orange:#ef7d31;
  --red:#e0483c;
  --yellow:#f2c230;
  --grad:linear-gradient(120deg,#a9d562 0%,#6cc79a 45%,#3fb3c4 100%);
  --photo:linear-gradient(135deg,#e6e2dc 0%,#c9c2b8 55%,#a9a298 100%);
  --photo-cool:linear-gradient(135deg,#dfe4e6 0%,#bcc6ca 60%,#9aa6ab 100%);
}
*{box-sizing:border-box;margin:0;padding:0}
html,body{width:1200px;height:4500px;overflow:hidden;background:#ffffff}
body{font-family:"Open Sans",Arial,sans-serif;color:var(--text)}
.deck{display:grid;grid-template-columns:repeat(3,384px);column-gap:12px;row-gap:81px;padding:30px 6px}
.slide{position:relative;width:384px;height:216px;background:#fff;overflow:hidden;box-shadow:0 0 0 1px #e8e8e8}
.abs{position:absolute}
.grad{background:var(--grad)}
.photo{background:var(--photo)}
.photo-cool{background:var(--photo-cool)}
.title{position:absolute;left:14px;top:12px;font-family:"Abel",sans-serif;font-size:11px;color:var(--ink);letter-spacing:.2px}
.brand{position:absolute;right:10px;top:9px;display:flex;align-items:center;gap:3px;font-family:"Abel",sans-serif;font-size:6px;font-weight:700;color:var(--ink);letter-spacing:.4px}
.brand i{display:block;width:7px;height:7px;background:var(--green)}
.brand.light{color:#fff}
.brand.light i{background:#fff}
.foot{position:absolute;left:0;right:0;bottom:0;height:5px;background:var(--green)}
.foot::after{content:"";position:absolute;right:10px;bottom:0;width:10px;height:10px;background:var(--ink)}
.p{font-size:5px;line-height:1.5;color:var(--text)}
.p.w{color:#fff}
.h{font-family:"Abel",sans-serif;font-size:7px;color:var(--ink);margin-bottom:2px}
.h.w{color:#fff}
.big{font-family:"Abel",sans-serif;color:#fff}
.item{display:flex;gap:5px;align-items:flex-start;margin-bottom:7px}
.tick{flex:none;width:9px;height:9px;border-radius:50%;background:var(--green);color:#fff;font-size:6px;line-height:9px;text-align:center}
.tick.dark{background:var(--ink)}
.tick.blue{background:var(--blue)}
.tick.white{background:#fff;color:var(--green)}
.sq{flex:none;width:9px;height:9px;background:var(--ink)}
.badge{position:absolute;background:#d6d6d6}
.col{position:absolute}
table.plan{border-collapse:collapse;font-size:5px;color:var(--text)}
table.plan th{color:#fff;font-weight:600;padding:3px 6px;text-align:left}
table.plan td{padding:2.5px 6px;border-bottom:1px solid #e5e5e5}
.price{position:absolute;top:60px;width:62px;height:98px;background:#fff;text-align:center}
.price b{display:block;margin:8px auto 6px;width:40px;height:16px;line-height:16px;color:#fff;font-size:8px}
.box4{position:absolute;top:50px;width:68px;height:104px;text-align:center;padding-top:10px}
.box4 .ic{width:20px;height:20px;margin:0 auto 8px;border-radius:50%;background:rgba(255,255,255,.9)}
</style>
</head>
<body>
<main class="deck">

<!-- 1 cover -->
<section class="slide grad">
  <div class="abs" style="left:52px;top:80px;display:flex;align-items:center;gap:10px">
    <span style="display:block;width:30px;height:30px;background:#fff"></span>
    <span class="big" style="font-size:24px;letter-spacing:1px">BRIGHT LANTERN WORKS</span>
  </div>
</section>

<!-- 2 intro -->
<section class="slide">
  <div class="brand" style="left:126px;right:auto;top:10px"><i></i>BRIGHT LANTERN WORKS</div>
  <div class="abs photo" role="img" aria-label="Portrait photo of a smiling consultant in a suit" style="left:118px;top:26px;width:152px;height:124px"></div>
  <div class="abs grad" style="left:0;top:140px;width:384px;height:40px"></div>
  <div class="abs big" style="left:0;top:150px;width:384px;text-align:center;font-size:12px">Your Title Goes Here</div>
  <div class="abs p" style="left:30px;top:192px;width:330px;display:flex;justify-content:space-between">
    <span>● Phone Line</span><span>● Email Here</span><span>● Website</span><span>● Address</span>
  </div>
</section>

<!-- 3 quote -->
<section class="slide grad">
  <div class="abs photo" role="img" aria-label="Soft photo of a team meeting under a green tint" style="inset:0;opacity:.25"></div>
  <div class="abs" style="left:228px;top:34px;width:22px;height:22px;border-radius:50%;background:#fff;color:var(--teal);font-size:16px;line-height:26px;text-align:center;font-family:Georgia,serif">“</div>
  <div class="abs p w" style="left:228px;top:66px;width:130px;font-size:6px">Coming together is a beginning, keeping together is progress, working together is success.</div>
</section>

<!-- 4 agenda -->
<section class="slide">
  <div class="title">Our Agenda</div><div class="brand"><i></i>BRIGHT LANTERN WORKS</div>
  <div class="col" style="left:30px;top:45px;width:150px">
    <div class="item"><span class="sq"></span><div><div class="h">Agenda One</div><div class="p">Short line of text about the topic.</div></div></div>
    <div class="item"><span class="sq"></span><div><div class="h">Agenda Two</div><div class="p">Short line of text about the topic.</div></div></div>
    <div class="item"><span class="sq"></span><div><div class="h">Agenda Three</div><div class="p">Short line of text about the topic.</div></div></div>
  </div>
  <div class="col" style="left:200px;top:45px;width:150px">
    <div class="item"><span class="sq"></span><div><div class="h">Agenda Four</div><div class="p">Short line of text about the topic.</div></div></div>
    <div class="item"><span class="sq"></span><div><div class="h">Agenda Five</div><div class="p">Short line of text about the topic.</div></div></div>
    <div class="item"><span class="sq"></span><div><div class="h">Agenda Six</div><div class="p">Short line of text about the topic.</div></div></div>
  </div>
  <div class="foot"></div>
</section>

<!-- 5 about -->
<section class="slide">
  <div class="abs photo" role="img" aria-label="Photo of hands writing at a desk" style="inset:0"></div>
  <div class="abs grad" style="left:186px;top:56px;width:198px;height:96px;opacity:.95"></div>
  <div class="abs" style="left:200px;top:66px;width:170px">
    <div class="big" style="font-size:11px;margin-bottom:6px">About Us</div>
    <div class="p w">This is a place for your header text. Insert your text here, just replace this text with your own words.</div>
  </div>
</section>

<!-- 6 services -->
<section class="slide">
  <div class="title">Our Services</div><div class="brand"><i></i>BRIGHT LANTERN WORKS</div>
  <div class="abs photo" role="img" aria-label="Photo of a consultant writing notes" style="left:14px;top:34px;width:150px;height:108px"></div>
  <div class="abs p" style="left:14px;top:148px;width:150px">Your text here. Short service summary line.</div>
  <div class="col" style="left:190px;top:40px;width:170px">
    <div class="item"><span class="tick">✓</span><div><div class="h">Service Number One</div><div class="p">Insert your text here, replace with your own.</div></div></div>
    <div class="item"><span class="tick">✓</span><div><div class="h">Service Number Two</div><div class="p">Insert your text here, replace with your own.</div></div></div>
    <div class="item"><span class="tick">✓</span><div><div class="h">Service Number Three</div><div class="p">Insert your text here, replace with your own.</div></div></div>
  </div>
  <div class="foot"></div>
</section>

<!-- 7 quote area -->
<section class="slide">
  <div class="title">Quote Area</div><div class="brand"><i></i>BRIGHT LANTERN WORKS</div>
  <div class="abs grad" style="left:0;top:36px;width:200px;height:130px"></div>
  <div class="abs p w" style="left:16px;top:70px;width:170px;font-size:6px">“Insert your quote text here, just replace this text with your own words and ideas.”</div>
  <div class="abs photo-cool" role="img" aria-label="Photo of an office workspace" style="left:200px;top:36px;width:184px;height:130px"></div>
  <div class="foot"></div>
</section>

<!-- 8 previous work -->
<section class="slide">
  <div class="badge" style="left:20px;top:22px;width:60px;height:22px;border-radius:3px"></div>
  <div class="badge" style="left:160px;top:18px;width:30px;height:30px;border-radius:50%"></div>
  <div class="badge" style="left:300px;top:24px;width:64px;height:18px"></div>
  <div class="badge" style="left:30px;top:96px;width:40px;height:24px"></div>
  <div class="badge" style="left:314px;top:94px;width:30px;height:30px;border-radius:50%"></div>
  <div class="badge" style="left:24px;top:168px;width:28px;height:28px;border-radius:50%"></div>
  <div class="badge" style="left:158px;top:172px;width:64px;height:20px;border-radius:3px"></div>
  <div class="badge" style="left:300px;top:170px;width:60px;height:24px"></div>
  <div class="abs" style="left:110px;top:80px;width:164px;height:56px;background:var(--green);color:#fff;font-family:'Abel',sans-serif;font-size:13px;text-align:center;line-height:56px">Our Previous work</div>
</section>

<!-- 9 text area -->
<section class="slide">
  <div class="title">Text Area</div><div class="brand"><i></i>BRIGHT LANTERN WORKS</div>
  <div class="abs" style="left:14px;top:38px;width:356px">
    <div class="h" style="font-size:7.5px">This is a place for your header text. Insert your text here, just replace this text with your own text.</div>
    <p class="p" style="margin-top:8px">Insert your paragraph here. Use this space to explain who you are, what you do and the value you bring to each client project you take on.</p>
    <p class="p" style="margin-top:6px">Insert your paragraph here. Use this space to explain who you are, what you do and the value you bring to each client project you take on.</p>
    <p class="p" style="margin-top:6px">Short closing line to wrap the text area neatly.</p>
  </div>
  <div class="foot"></div>
</section>

<!-- 10 vision -->
<section class="slide">
  <div class="title">Our Vision &amp; Mission</div><div class="brand"><i></i>BRIGHT LANTERN WORKS</div>
  <div class="abs grad" style="left:0;top:38px;width:384px;height:128px"></div>
  <div class="abs" style="left:20px;top:54px;width:160px"><div class="h w">Our Vision</div><div class="p w">Insert your text here. Describe where the company is heading and why it matters.</div></div>
  <div class="abs" style="left:204px;top:54px;width:160px"><div class="h w">Our Mission</div><div class="p w">Insert your text here. Describe how the team delivers value to every client.</div></div>
  <div class="foot"></div>
</section>

<!-- 11 framed text -->
<section class="slide" style="border:9px solid var(--ink);border-right-width:0">
  <div class="title" style="left:8px;top:6px">Text Area</div><div class="brand" style="top:4px"><i></i>BRIGHT LANTERN WORKS</div>
  <div class="abs" style="left:8px;top:32px;width:330px">
    <div class="h">This is a place for your header text. Insert your text here, just replace this text.</div>
    <p class="p" style="margin-top:6px">Insert your paragraph here. Use this space to share a longer description of the topic in plain words.</p>
    <p class="p" style="margin-top:6px">Insert your paragraph here. Use this space to share a longer description of the topic in plain words.</p>
  </div>
  <div class="abs" style="left:0;right:0;bottom:0;height:24px;background:var(--green)"></div>
</section>

<!-- 12 half photo -->
<section class="slide">
  <div class="abs photo" role="img" aria-label="Photo of a pen on paper with a green tint" style="left:0;top:0;width:190px;height:216px"></div>
  <div class="abs grad" style="left:0;top:0;width:190px;height:216px;opacity:.55"></div>
  <div class="brand light" style="left:40px;right:auto;top:98px;font-size:10px"><i style="width:11px;height:11px"></i>BRIGHT LANTERN WORKS</div>
  <div class="abs" style="left:206px;top:40px;width:160px">
    <div class="big" style="color:var(--ink);font-size:11px;margin-bottom:6px">Your Title Goes Here</div>
    <div class="p" style="margin-bottom:10px">Insert your text here, replace with your own words.</div>
    <div class="item"><span class="tick">✓</span><div class="p">First point goes here</div></div>
    <div class="item"><span class="tick">✓</span><div class="p">Second point goes here</div></div>
  </div>
  <div class="foot"></div>
</section>

<!-- 13 image grid -->
<section class="slide">
  <div class="title">Your Title Goes Here</div><div class="brand"><i></i>BRIGHT LANTERN WORKS</div>
  <div class="abs photo" role="img" aria-label="Photo of hands typing on a laptop" style="left:14px;top:34px;width:70px;height:54px"></div>
  <div class="abs" style="left:88px;top:34px;width:70px;height:54px;background:var(--green)"></div>
  <div class="abs photo-cool" role="img" aria-label="Photo of a notebook and pen" style="left:162px;top:34px;width:70px;height:54px"></div>
  <div class="abs" style="left:14px;top:92px;width:70px;height:54px;background:var(--orange)"></div>
  <div class="abs photo" role="img" aria-label="Photo of a desk with documents" style="left:88px;top:92px;width:70px;height:54px"></div>
  <div class="abs" style="left:162px;top:92px;width:70px;height:54px;background:var(--blue)"></div>
  <div class="abs" style="left:248px;top:40px;width:120px"><div class="h">Heading Goes Here</div><div class="p">Insert your text here, just replace this text with your own words.</div></div>
  <div class="foot"></div>
</section>

<!-- 14 photo + green panel -->
<section class="slide">
  <div class="abs photo" role="img" aria-label="Photo of a consultant writing at a desk" style="left:0;top:0;width:200px;height:216px"></div>
  <div class="abs" style="left:200px;top:0;width:184px;height:216px;background:var(--green)"></div>
  <div class="brand light"><i></i>BRIGHT LANTERN WORKS</div>
  <div class="abs" style="left:214px;top:40px;width:158px">
    <div class="p w" style="font-size:6px;margin-bottom:10px">This is a place for your header text. Insert your text here, just replace it.</div>
    <div class="item"><span class="tick white">✓</span><div class="p w">Point one text here</div></div>
    <div class="item"><span class="tick white">✓</span><div class="p w">Point two text here</div></div>
    <div class="item"><span class="tick white">✓</span><div class="p w">Point three text here</div></div>
  </div>
</section>

<!-- 15 collage -->
<section class="slide">
  <div class="brand"><i></i>BRIGHT LANTERN WORKS</div>
  <div class="abs photo-cool" role="img" aria-label="Photo of a hand holding a pen" style="left:0;top:0;width:110px;height:100px"></div>
  <div class="abs grad" style="left:110px;top:0;width:100px;height:100px"></div>
  <div class="brand light" style="left:116px;right:auto;top:44px"><i></i>BRIGHT LANTERN WORKS</div>
  <div class="abs photo" role="img" aria-label="Photo of pencils in a cup" style="left:0;top:100px;width:210px;height:116px"></div>
  <div class="abs" style="left:226px;top:60px;width:140px">
    <div class="big" style="color:var(--ink);font-size:12px;margin-bottom:6px">Your Title<br>Goes Here</div>
    <div class="p">Insert your text here, just replace this text with your own.</div>
  </div>
  <div class="foot"></div>
</section>

<!-- 16 text + photos -->
<section class="slide">
  <div class="title">Your Title Goes Here</div><div class="brand"><i></i>BRIGHT LANTERN WORKS</div>
  <div class="abs" style="left:14px;top:38px;width:170px">
    <div class="h">This is a place for your header text. Insert your text here.</div>
    <p class="p" style="margin-top:6px">Insert your paragraph here. Replace this text with a short description of your work and ideas.</p>
  </div>
  <div class="abs photo" role="img" aria-label="Photo of notebooks" style="left:200px;top:36px;width:80px;height:62px"></div>
  <div class="abs photo-cool" role="img" aria-label="Photo of a desk" style="left:284px;top:36px;width:80px;height:62px"></div>
  <div class="abs photo-cool" role="img" aria-label="Photo of a tablet" style="left:200px;top:102px;width:80px;height:62px"></div>
  <div class="abs photo" role="img" aria-label="Photo of hands on paper" style="left:284px;top:102px;width:80px;height:62px"></div>
  <div class="foot"></div>
</section>

<!-- 17 portfolio -->
<section class="slide">
  <div class="title">Portfolio Area</div><div class="brand"><i></i>BRIGHT LANTERN WORKS</div>
  <div class="col" style="left:14px;top:36px;width:170px">
    <div class="h">Heading Goes Here</div><div class="p" style="margin-bottom:8px">Insert your text here, replace it.</div>
    <div class="item"><span class="tick">✓</span><div><div class="h">Your Title Here</div><div class="p">Short project note.</div></div></div>
    <div class="item"><span class="tick">✓</span><div><div class="h">Your Title Here</div><div class="p">Short project note.</div></div></div>
    <div class="item"><span class="tick">✓</span><div><div class="h">Your Title Here</div><div class="p">Short project note.</div></div></div>
  </div>
  <div class="abs photo-cool" role="img" aria-label="Photo of pencils in a holder" style="left:196px;top:30px;width:86px;height:70px"></div>
  <div class="abs photo" role="img" aria-label="Photo of a white desk" style="left:286px;top:30px;width:86px;height:70px"></div>
  <div class="abs photo" role="img" aria-label="Photo of office supplies" style="left:196px;top:104px;width:86px;height:70px"></div>
  <div class="abs photo-cool" role="img" aria-label="Photo of a notepad" style="left:286px;top:104px;width:86px;height:70px"></div>
  <div class="foot"></div>
</section>

<!-- 18 product -->
<section class="slide">
  <div class="title">Your Title Goes Here</div><div class="brand"><i></i>BRIGHT LANTERN WORKS</div>
  <div class="col" style="left:14px;top:36px;width:180px">
    <div class="h">Heading Goes Here</div><div class="p" style="margin-bottom:8px">Insert your text here, replace it.</div>
    <div class="item"><span class="tick">✓</span><div><div class="h">Your Title Here</div><div class="p">Short product note.</div></div></div>
    <div class="item"><span class="tick">✓</span><div><div class="h">Your Title Here</div><div class="p">Short product note.</div></div></div>
    <div class="item"><span class="tick">✓</span><div><div class="h">Your Title Here</div><div class="p">Short product note.</div></div></div>
  </div>
  <div class="abs photo-cool" role="img" aria-label="Product photo of a compact device" style="left:230px;top:56px;width:120px;height:90px"></div>
  <div class="foot"></div>
</section>

<!-- 19 differences -->
<section class="slide">
  <div class="title">Our Differences</div><div class="brand"><i></i>BRIGHT LANTERN WORKS</div>
  <div class="abs grad" style="left:14px;top:36px;width:180px;height:130px"></div>
  <div class="col" style="left:24px;top:48px;width:160px">
    <div class="item"><span class="tick white">✓</span><div class="p w">Difference one text here</div></div>
    <div class="item"><span class="tick white">✓</span><div class="p w">Difference two text here</div></div>
    <div class="item"><span class="tick white">✓</span><div class="p w">Difference three text here</div></div>
    <div class="item"><span class="tick white">✓</span><div class="p w">Difference four text here</div></div>
  </div>
  <div class="abs photo" role="img" aria-label="Photo of a hand writing on paper" style="left:194px;top:36px;width:176px;height:130px"></div>
  <div class="foot"></div>
</section>

<!-- 20 two columns -->
<section class="slide">
  <div class="title">Two Column Description</div><div class="brand"><i></i>BRIGHT LANTERN WORKS</div>
  <div class="abs h" style="left:14px;top:36px;width:340px">This is a place for your header text. Insert your text here, just replace this text with your own.</div>
  <div class="abs" style="left:14px;top:64px;width:168px"><div class="h">Heading Goes Here</div><p class="p">Insert your paragraph here. Replace this text with a short description in your own words.</p></div>
  <div class="abs" style="left:200px;top:64px;width:168px"><div class="h">Heading Goes Here</div><p class="p">Insert your paragraph here. Replace this text with a short description in your own words.</p></div>
  <div class="foot"></div>
</section>

<!-- 21 break -->
<section class="slide" style="background:linear-gradient(135deg,#4fae6c,#2e8f6a 60%,#2a7f6e)">
  <div class="abs big" style="right:14px;top:12px;font-size:11px">Aldenmoor</div>
  <svg class="abs" style="left:180px;top:84px" width="24" height="22" viewBox="0 0 24 22"><path d="M3 6h14v8a6 6 0 0 1-6 6H9a6 6 0 0 1-6-6z" fill="none" stroke="#fff" stroke-width="1.5"/><path d="M17 8h2a3 3 0 0 1 0 6h-2" fill="none" stroke="#fff" stroke-width="1.5"/></svg>
  <div class="abs big" style="left:0;top:110px;width:384px;text-align:center;font-size:9px;letter-spacing:1px">COFFEE BREAK</div>
  <div class="abs p w" style="left:0;top:122px;width:384px;text-align:center">Back in 15 minutes</div>
</section>

<!-- 22 three columns -->
<section class="slide">
  <div class="title">Three Column Description</div><div class="brand"><i></i>BRIGHT LANTERN WORKS</div>
  <div class="abs h" style="left:14px;top:36px;width:340px">This is a place for your header text. Insert your text here, just replace this text with your own.</div>
  <div class="abs" style="left:14px;top:66px;width:108px"><div class="h">Heading Here</div><p class="p">Insert your paragraph here. Replace with a short description.</p></div>
  <div class="abs" style="left:136px;top:66px;width:108px"><div class="h">Heading Here</div><p class="p">Insert your paragraph here. Replace with a short description.</p></div>
  <div class="abs" style="left:258px;top:66px;width:108px"><div class="h">Heading Here</div><p class="p">Insert your paragraph here. Replace with a short description.</p></div>
  <div class="foot"></div>
</section>

<!-- 23 overlay -->
<section class="slide">
  <div class="abs photo" role="img" aria-label="Photo of a consultant writing at a white desk" style="inset:0"></div>
  <div class="abs grad" style="left:200px;top:0;width:184px;height:216px;opacity:.92"></div>
  <div class="brand light"><i></i>BRIGHT LANTERN WORKS</div>
  <div class="abs big" style="left:216px;top:90px;font-size:13px">Your Title Goes<br>Here</div>
</section>

<!-- 24 numbered -->
<section class="slide">
  <div class="title">Your Title Goes Here</div><div class="brand"><i></i>BRIGHT LANTERN WORKS</div>
  <div class="col" style="left:14px;top:40px;width:170px">
    <div class="item"><span class="tick">✓</span><div><div class="h">Service Number One</div><div class="p">Insert your text here.</div></div></div>
    <div class="item"><span class="tick">✓</span><div><div class="h">Service Number Two</div><div class="p">Insert your text here.</div></div></div>
    <div class="item"><span class="tick">✓</span><div><div class="h">Service Number Three</div><div class="p">Insert your text here.</div></div></div>
  </div>
  <div class="abs" style="left:200px;top:40px;width:170px;height:30px;background:var(--ink)"></div>
  <div class="abs" style="left:200px;top:76px;width:170px;height:30px;background:var(--green)"></div>
  <div class="abs" style="left:200px;top:112px;width:170px;height:30px;background:var(--blue)"></div>
  <div class="abs big" style="left:206px;top:42px;font-size:20px;line-height:26px">1</div>
  <div class="abs big" style="left:206px;top:78px;font-size:20px;line-height:26px">2</div>
  <div class="abs big" style="left:206px;top:114px;font-size:20px;line-height:26px">3</div>
  <div class="abs p w" style="left:226px;top:50px;width:136px">Insert your text here, replace it.</div>
  <div class="abs p w" style="left:226px;top:86px;width:136px">Insert your text here, replace it.</div>
  <div class="abs p w" style="left:226px;top:122px;width:136px">Insert your text here, replace it.</div>
  <div class="foot"></div>
</section>

<!-- 25 four bullets -->
<section class="slide">
  <div class="title">Four Bullets with Paragraph</div><div class="brand"><i></i>BRIGHT LANTERN WORKS</div>
  <div class="abs" style="left:14px;top:38px;width:160px"><div class="h">This is a place for your header text.</div><p class="p">Insert your paragraph here, replace it.</p></div>
  <div class="abs" style="left:200px;top:38px;width:160px"><div class="h">Heading Goes Here</div><p class="p">Insert your paragraph here, replace it.</p></div>
  <div class="col" style="left:14px;top:100px;width:170px">
    <div class="item"><span class="tick">✓</span><div><div class="h">Your Title Here</div><div class="p">Short note.</div></div></div>
    <div class="item"><span class="tick dark">✓</span><div><div class="h">Your Title Here</div><div class="p">Short note.</div></div></div>
  </div>
  <div class="col" style="left:200px;top:100px;width:170px">
    <div class="item"><span class="tick">✓</span><div><div class="h">Your Title Here</div><div class="p">Short note.</div></div></div>
    <div class="item"><span class="tick dark">✓</span><div><div class="h">Your Title Here</div><div class="p">Short note.</div></div></div>
  </div>
  <div class="foot"></div>
</section>

<!-- 26 your title -->
<section class="slide">
  <div class="title">Your Title</div><div class="brand"><i></i>BRIGHT LANTERN WORKS</div>
  <div class="abs" style="left:14px;top:38px;width:100px"><div class="h">Heading Goes Here</div><p class="p">Insert your paragraph here. Replace with your own words.</p></div>
  <div class="abs photo" role="img" aria-label="Photo of a consultant at work" style="left:124px;top:30px;width:120px;height:150px"></div>
  <div class="col" style="left:256px;top:40px;width:116px">
    <div class="item"><span class="tick">✓</span><div class="p">Your text here</div></div>
    <div class="item"><span class="tick">✓</span><div class="p">Your text here</div></div>
    <div class="item"><span class="tick">✓</span><div class="p">Your text here</div></div>
    <div class="item"><span class="tick">✓</span><div class="p">Your text here</div></div>
  </div>
  <div class="foot"></div>
</section>

<!-- 27 text & bullet -->
<section class="slide">
  <div class="title">Text &amp; Bullet Area</div><div class="brand"><i></i>BRIGHT LANTERN WORKS</div>
  <div class="abs" style="left:14px;top:38px;width:170px"><div class="h">Heading Goes Here</div><p class="p">Insert your paragraph here. Replace this text with a short description in your own words and ideas.</p></div>
  <div class="col" style="left:210px;top:38px;width:160px">
    <div class="item"><span class="tick">✓</span><div><div class="h">Your Title Here</div><div class="p">Short note.</div></div></div>
    <div class="item"><span class="tick">✓</span><div><div class="h">Your Title Here</div><div class="p">Short note.</div></div></div>
    <div class="item"><span class="tick">✓</span><div><div class="h">Your Title Here</div><div class="p">Short note.</div></div></div>
    <div class="item"><span class="tick">✓</span><div><div class="h">Your Title Here</div><div class="p">Short note.</div></div></div>
  </div>
  <div class="foot"></div>
</section>

<!-- 28 section -->
<section class="slide grad">
  <div class="abs photo" role="img" aria-label="Faint photo of a hand writing" style="inset:0;opacity:.2"></div>
  <div class="brand light" style="right:40px;top:60px;font-size:11px"><i style="width:12px;height:12px"></i>BRIGHT LANTERN WORKS</div>
  <div class="abs big" style="left:30px;top:150px;font-size:11px">Your Title Goes Here</div>
</section>

<!-- 29 paragraph three bullet -->
<section class="slide">
  <div class="title">Paragraph with Three Bullet</div><div class="brand"><i></i>BRIGHT LANTERN WORKS</div>
  <div class="abs h" style="left:14px;top:36px;width:340px">This is a place for your header text. Insert your text here, just replace this text with your own.</div>
  <div class="abs" style="left:14px;top:70px;width:108px"><span class="tick" style="display:block;margin-bottom:4px">✓</span><div class="h">Heading Here</div><p class="p">Insert your text here.</p></div>
  <div class="abs" style="left:136px;top:70px;width:108px"><span class="tick dark" style="display:block;margin-bottom:4px">✓</span><div class="h">Heading Here</div><p class="p">Insert your text here.</p></div>
  <div class="abs" style="left:258px;top:70px;width:108px"><span class="tick blue" style="display:block;margin-bottom:4px">✓</span><div class="h">Heading Here</div><p class="p">Insert your text here.</p></div>
  <div class="foot"></div>
</section>

<!-- 30 global -->
<section class="slide">
  <div class="title">Global Experience</div><div class="brand"><i></i>BRIGHT LANTERN WORKS</div>
  <div class="abs" role="img" aria-label="World map with location markers" style="left:120px;top:34px;width:250px;height:130px;background:linear-gradient(135deg,#e4e4e4,#cfcfcf)"></div>
  <div class="abs" style="left:14px;top:140px;width:100px"><div class="item"><span class="tick">✓</span><div><div class="h">Heading Goes Here</div><div class="p">Short note.</div></div></div></div>
  <div class="foot"></div>
</section>

<!-- 31 multiple column -->
<section class="slide">
  <div class="title">Multiple Column Area</div><div class="brand"><i></i>BRIGHT LANTERN WORKS</div>
  <div class="abs" style="left:14px;top:40px;width:356px;display:flex;justify-content:space-between">
    <div style="width:80px;text-align:center"><span class="tick dark" style="display:inline-block;width:16px;height:16px;line-height:16px"></span><div class="p">Your text here</div></div>
    <div style="width:80px;text-align:center"><span class="tick" style="display:inline-block;width:16px;height:16px;line-height:16px"></span><div class="p">Your text here</div></div>
    <div style="width:80px;text-align:center"><span class="tick blue" style="display:inline-block;width:16px;height:16px;line-height:16px"></span><div class="p">Your text here</div></div>
    <div style="width:80px;text-align:center"><span class="tick dark" style="display:inline-block;width:16px;height:16px;line-height:16px"></span><div class="p">Your text here</div></div>
  </div>
  <div class="abs" style="left:14px;top:100px;width:168px"><div class="h">Heading Goes Here</div><p class="p">Insert your paragraph here, replace with your own words.</p></div>
  <div class="abs" style="left:200px;top:100px;width:168px"><div class="h">Heading Goes Here</div><p class="p">Insert your paragraph here, replace with your own words.</p></div>
  <div class="foot"></div>
</section>

<!-- 32 pricing -->
<section class="slide">
  <div class="title">Monthly Subscription</div><div class="brand"><i></i>BRIGHT LANTERN WORKS</div>
  <div class="abs" style="left:0;top:86px;width:384px;height:56px;background:var(--blue)"></div>
  <div class="price" style="left:100px"><b style="background:var(--red)">$300</b><div class="p">Basic plan<br>Item one<br>Item two</div></div>
  <div class="price" style="left:161px"><b style="background:var(--orange)">$500</b><div class="p">Pro plan<br>Item one<br>Item two</div></div>
  <div class="price" style="left:222px"><b style="background:var(--green)">$400</b><div class="p">Team plan<br>Item one<br>Item two</div></div>
  <div class="foot"></div>
</section>

<!-- 33 section -->
<section class="slide grad">
  <div class="abs photo" role="img" aria-label="Faint photo of a pen on paper" style="inset:0;opacity:.2"></div>
  <div class="abs big" style="left:0;top:98px;width:384px;text-align:center;font-size:11px">Your Title Goes Here</div>
</section>

<!-- 34 video -->
<section class="slide">
  <div class="abs big" style="left:14px;top:34px;color:var(--ink);font-size:12px">Video Title<br>Goes Here</div>
  <div class="abs p" style="left:14px;top:70px;width:90px">Insert your text here, replace it.</div>
  <div class="brand"><i></i>BRIGHT LANTERN WORKS</div>
  <div class="abs photo-cool" role="img" aria-label="Desktop monitor showing a video still" style="left:120px;top:30px;width:200px;height:140px"></div>
  <div class="foot"></div>
</section>

<!-- 35 four boxes -->
<section class="slide">
  <div class="title">Four Column Area</div><div class="brand"><i></i>BRIGHT LANTERN WORKS</div>
  <div class="box4" style="left:44px;background:var(--orange)"><div class="ic"></div><div class="p w">Your text here</div></div>
  <div class="box4" style="left:118px;background:var(--teal)"><div class="ic"></div><div class="p w">Your text here</div></div>
  <div class="box4" style="left:192px;background:var(--red)"><div class="ic"></div><div class="p w">Your text here</div></div>
  <div class="box4" style="left:266px;background:var(--green)"><div class="ic"></div><div class="p w">Your text here</div></div>
  <div class="foot"></div>
</section>

<!-- 36 four rings -->
<section class="slide">
  <div class="title">Four Column Area</div><div class="brand"><i></i>BRIGHT LANTERN WORKS</div>
  <svg class="abs" style="left:30px;top:56px" width="324" height="50" viewBox="0 0 324 50">
    <circle cx="36" cy="25" r="20" fill="none" stroke="#1f1f1f" stroke-width="5"/>
    <circle cx="120" cy="25" r="20" fill="none" stroke="#3fb6a8" stroke-width="5"/>
    <circle cx="204" cy="25" r="20" fill="none" stroke="#9a9a9a" stroke-width="5"/>
    <circle cx="288" cy="25" r="20" fill="none" stroke="#8cc63f" stroke-width="5"/>
  </svg>
  <div class="abs p" style="left:30px;top:118px;width:324px;display:flex;justify-content:space-around;text-align:center"><span>Text here</span><span>Text here</span><span>Text here</span><span>Text here</span></div>
  <div class="foot"></div>
</section>

<!-- 37 key points -->
<section class="slide">
  <div class="title">Key Points Area</div><div class="brand"><i></i>BRIGHT LANTERN WORKS</div>
  <svg class="abs" style="left:60px;top:50px" width="264" height="60" viewBox="0 0 264 60">
    <circle cx="36" cy="30" r="28" fill="#ef7d31" opacity=".9"/>
    <circle cx="98" cy="30" r="28" fill="#3fb6a8" opacity=".9"/>
    <circle cx="160" cy="30" r="28" fill="#8cc63f" opacity=".9"/>
    <circle cx="222" cy="30" r="28" fill="#f2c230" opacity=".9"/>
  </svg>
  <div class="abs p" style="left:60px;top:124px;width:264px;display:flex;justify-content:space-around;text-align:center"><span>Point one</span><span>Point two</span><span>Point three</span><span>Point four</span></div>
  <div class="foot"></div>
</section>

<!-- 38 workflow -->
<section class="slide">
  <div class="title">Workflow Area</div><div class="brand"><i></i>BRIGHT LANTERN WORKS</div>
  <svg class="abs" style="left:30px;top:60px" width="324" height="70" viewBox="0 0 324 70">
    <path d="M6 40a34 34 0 0 1 68 0" fill="none" stroke="#1f1f1f" stroke-width="10"/>
    <path d="M86 30a34 34 0 0 0 68 0" fill="none" stroke="#8cc63f" stroke-width="10"/>
    <path d="M166 40a34 34 0 0 1 68 0" fill="none" stroke="#1f1f1f" stroke-width="10"/>
    <path d="M246 30a34 34 0 0 0 68 0" fill="none" stroke="#8cc63f" stroke-width="10"/>
  </svg>
  <div class="abs p" style="left:30px;top:140px;width:324px;display:flex;justify-content:space-around"><span>Step 1</span><span>Step 2</span><span>Step 3</span><span>Step 4</span></div>
  <div class="foot"></div>
</section>

<!-- 39 timeline -->
<section class="slide">
  <div class="title">Timeline</div><div class="brand"><i></i>BRIGHT LANTERN WORKS</div>
  <svg class="abs" style="left:20px;top:60px" width="344" height="90" viewBox="0 0 344 90">
    <line x1="0" y1="45" x2="344" y2="45" stroke="#c8c8c8" stroke-width="2"/>
    <line x1="70" y1="20" x2="70" y2="70" stroke="#c8c8c8"/><line x1="172" y1="20" x2="172" y2="70" stroke="#c8c8c8"/><line x1="274" y1="20" x2="274" y2="70" stroke="#c8c8c8"/>
    <circle cx="70" cy="45" r="14" fill="#2d9fd8"/><circle cx="172" cy="45" r="14" fill="#3fb6a8"/><circle cx="274" cy="45" r="14" fill="#8cc63f"/>
  </svg>
  <div class="abs p" style="left:70px;top:62px">2019</div><div class="abs p" style="left:172px;top:142px">2021</div><div class="abs p" style="left:274px;top:62px">2023</div>
  <div class="abs p" style="left:14px;top:180px">Your Title Here</div>
  <div class="foot"></div>
</section>

<!-- 40 team -->
<section class="slide">
  <div class="title">Our Team</div><div class="brand"><i></i>BRIGHT LANTERN WORKS</div>
  <div class="abs photo" role="img" aria-label="Team member portrait" style="left:14px;top:38px;width:30px;height:30px;border-radius:50%"></div>
  <div class="abs" style="left:50px;top:40px"><div class="h">Anna Reeve</div><div class="p">Director</div></div>
  <div class="abs photo" role="img" aria-label="Team member portrait" style="left:200px;top:38px;width:30px;height:30px;border-radius:50%"></div>
  <div class="abs" style="left:236px;top:40px"><div class="h">Tom Vale</div><div class="p">Consultant</div></div>
  <div class="abs photo" role="img" aria-label="Team member portrait" style="left:14px;top:100px;width:30px;height:30px;border-radius:50%"></div>
  <div class="abs" style="left:50px;top:102px"><div class="h">Lena Marsh</div><div class="p">Analyst</div></div>
  <div class="abs photo" role="img" aria-label="Team member portrait" style="left:200px;top:100px;width:30px;height:30px;border-radius:50%"></div>
  <div class="abs" style="left:236px;top:102px"><div class="h">Omar Kent</div><div class="p">Strategist</div></div>
  <div class="foot"></div>
</section>

<!-- 41 testimonials -->
<section class="slide">
  <div class="title">Customer Testimonials</div><div class="brand"><i></i>BRIGHT LANTERN WORKS</div>
  <div class="abs photo" role="img" aria-label="Client portrait" style="left:168px;top:32px;width:48px;height:48px;border-radius:50%"></div>
  <div class="abs grad" style="left:0;top:96px;width:384px;height:60px"></div>
  <div class="abs p w" style="left:60px;top:110px;width:264px;text-align:center;font-size:6px">“Insert the client testimonial here, just replace this text with their own words.”</div>
  <div class="abs" style="left:0;top:156px;width:384px;height:10px;background:var(--blue)"></div>
  <div class="foot"></div>
</section>

<!-- 42 bar chart -->
<section class="slide">
  <div class="title">Bullet &amp; Chart Area</div><div class="brand"><i></i>BRIGHT LANTERN WORKS</div>
  <svg class="abs" style="left:14px;top:40px" width="200" height="130" viewBox="0 0 200 130">
    <line x1="20" y1="0" x2="20" y2="124" stroke="#cfcfcf"/>
    <rect x="20" y="6" width="150" height="7" fill="#1f1f1f"/><rect x="20" y="15" width="110" height="7" fill="#8cc63f"/>
    <rect x="20" y="36" width="120" height="7" fill="#1f1f1f"/><rect x="20" y="45" width="160" height="7" fill="#2d9fd8"/>
    <rect x="20" y="66" width="90" height="7" fill="#1f1f1f"/><rect x="20" y="75" width="130" height="7" fill="#8cc63f"/>
    <rect x="20" y="96" width="140" height="7" fill="#1f1f1f"/><rect x="20" y="105" width="100" height="7" fill="#2d9fd8"/>
  </svg>
  <div class="col" style="left:240px;top:44px;width:130px">
    <div class="item"><span class="tick">✓</span><div><div class="h">Category One</div><div class="p">Short note.</div></div></div>
    <div class="item"><span class="tick dark">✓</span><div><div class="h">Category Two</div><div class="p">Short note.</div></div></div>
    <div class="item"><span class="tick blue">✓</span><div><div class="h">Category Three</div><div class="p">Short note.</div></div></div>
  </div>
  <div class="foot"></div>
</section>

<!-- 43 table -->
<section class="slide">
  <div class="title">Table Area</div><div class="brand"><i></i>BRIGHT LANTERN WORKS</div>
  <table class="plan abs" style="left:14px;top:36px;width:220px">
    <tr><th style="background:var(--ink)">Description</th><th style="background:var(--blue)">Basic</th><th style="background:var(--green)">Pro</th></tr>
    <tr><td>Strategy review</td><td>✓</td><td>✓</td></tr>
    <tr><td>Market analysis</td><td>✓</td><td>✓</td></tr>
    <tr><td>Process audit</td><td>–</td><td>✓</td></tr>
    <tr><td>Team workshop</td><td>✓</td><td>✓</td></tr>
    <tr><td>Monthly report</td><td>–</td><td>✓</td></tr>
    <tr><td>Price</td><td>$300</td><td>$500</td></tr>
  </table>
  <div class="abs" style="left:250px;top:40px;width:120px"><div class="h">Heading Goes Here</div><p class="p">Insert your text here, replace with your own words.</p></div>
  <div class="foot"></div>
</section>

<!-- 44 donut -->
<section class="slide">
  <div class="title">Bullet &amp; Chart Area</div><div class="brand"><i></i>BRIGHT LANTERN WORKS</div>
  <div class="col" style="left:14px;top:38px;width:160px">
    <div class="item"><span class="tick">✓</span><div><div class="h">Your Title Here</div><div class="p">Short note.</div></div></div>
    <div class="item"><span class="tick dark">✓</span><div><div class="h">Your Title Here</div><div class="p">Short note.</div></div></div>
    <div class="item"><span class="tick">✓</span><div><div class="h">Your Title Here</div><div class="p">Short note.</div></div></div>
    <div class="item"><span class="tick dark">✓</span><div><div class="h">Your Title Here</div><div class="p">Short note.</div></div></div>
  </div>
  <svg class="abs" style="left:226px;top:50px" width="100" height="100" viewBox="0 0 100 100">
    <circle cx="50" cy="50" r="36" fill="none" stroke="#cfcfcf" stroke-width="14"/>
    <circle cx="50" cy="50" r="36" fill="none" stroke="#8cc63f" stroke-width="14" stroke-dasharray="135.7 226.2" transform="rotate(-90 50 50)"/>
  </svg>
  <div class="abs big" style="left:200px;top:120px;color:var(--green);font-size:10px">60%</div>
  <div class="abs big" style="left:336px;top:70px;color:var(--ink);font-size:10px">40%</div>
  <div class="foot"></div>
</section>

<!-- 45 contact -->
<section class="slide grad">
  <div class="abs photo" role="img" aria-label="Faint photo of a desk with a pen" style="inset:0;opacity:.2"></div>
  <div class="brand light" style="left:20px;right:auto;top:16px"><i></i>BRIGHT LANTERN WORKS</div>
  <div class="abs big" style="left:20px;top:80px;font-size:11px">Our Contact</div>
  <div class="abs p w" style="left:20px;top:96px;width:140px">Phone line here<br>Email address here<br>Office address here</div>
  <div class="abs big" style="right:24px;top:140px;font-size:12px">THANK YOU</div>
  <div class="abs" style="left:0;top:184px;width:384px;display:flex;justify-content:center;gap:6px">
    <span style="width:8px;height:8px;border-radius:50%;background:#fff"></span><span style="width:8px;height:8px;border-radius:50%;background:#fff"></span><span style="width:8px;height:8px;border-radius:50%;background:#fff"></span><span style="width:8px;height:8px;border-radius:50%;background:#fff"></span>
  </div>
</section>

</main>
</body>
</html>
```